Simple HVAC & Electrical Contractor Billboard

Leasing a 12'3" H by 49'3" W billboard. I'd like to use our current logo and add a few words to let people know what we do. Looking for a clean simple look.
Our company name is Harold Pruett Mechanical - What we are is Air Conditioning & Electrical Contractors.

Our license numbers are TACLA00052916K & TECL71420 they will need to be visible on the sign somewhere.

I'm not sure how much information I want to see on the sign. I want to keep it clean but some of our contact info is as follows. Office # 555-208-4619 - Webpage hpmexample.com. I feel like most people can search the name to find the contact info they need but I'll defer to the designers to come up with the best design.

I have attached a couple different logos we have used I the past.

```html
<!DOCTYPE html>
<html lang="en">
<head>
<meta charset="utf-8">
<title>Harold Pruett Mechanical – Billboard</title>
<link href="https://fonts.googleapis.com/css2?family=Open+Sans:wght@400;600;700;800&display=swap" rel="stylesheet">
<style>
  :root {
    --red: #ed1c24;
    --ink: #1f1d1e;
    --white: #ffffff;
    --stage: #d6d6d6;
  }
  * { box-sizing: border-box; margin: 0; padding: 0; }
  html, body {
    width: 1200px; height: 566px; overflow: hidden;
    background: var(--stage);
    font-family: "Open Sans", Arial, sans-serif;
  }
  .billboard {
    position: absolute; left: 20px; top: 138px;
    width: 1160px; height: 290px;
    background: var(--white);
    overflow: hidden;
  }
  .brand {
    position: absolute; left: 60px; top: 0; width: 300px; height: 222px;
    display: flex; align-items: center; justify-content: center; gap: 14px;
  }
  .brand-mark { width: 34px; height: 34px; background: var(--red); flex: none; }
  .brand-name {
    color: var(--ink); font-weight: 600; font-size: 25px; line-height: 1.12;
    letter-spacing: 0.5px; text-transform: uppercase;
  }
  .divider {
    position: absolute; left: 393px; top: 48px; width: 1px; height: 136px;
    background: var(--ink);
  }
  .headline {
    position: absolute; left: 420px; right: 20px; top: 58px;
    text-align: center; font-weight: 800; text-transform: uppercase;
    font-size: 50px; line-height: 60px; letter-spacing: 0.3px;
  }
  .headline .service { color: var(--red); display: block; }
  .headline .trade { color: var(--ink); display: block; }
  .info-band {
    position: absolute; left: 0; top: 222px; width: 1160px; height: 68px;
    background: var(--ink);
  }
  .licenses {
    position: absolute; left: 20px; width: 380px; top: 8px; text-align: center;
  }
  .licenses .label { color: var(--red); font-weight: 700; font-size: 14px; line-height: 20px; }
  .licenses .numbers { color: var(--white); font-weight: 700; font-size: 18px; line-height: 28px; }
  .phone-panel { position: absolute; left: 0; top: 0; }
  .contact {
    position: absolute; top: 0; height: 68px;
    display: flex; align-items: center; gap: 14px;
    color: var(--white); font-weight: 700;
  }
  .contact.phone { left: 441px; font-size: 28px; }
  .contact.web { left: 764px; font-size: 25px; }
  .icon { width: 40px; height: 40px; flex: none; }
</style>
</head>
<body>
  <div class="billboard">
    <div class="brand">
      <span class="brand-mark"></span>
      <span class="brand-name">Harold Pruett<br>Mechanical</span>
    </div>
    <div class="divider"></div>
    <h1 class="headline">
      <span class="service">Air Conditioning &amp;</span>
      <span class="trade">Electrical Contractors</span>
    </h1>

    <div class="info-band">
      <svg class="phone-panel" width="1160" height="68" viewBox="0 0 1160 68">
        <polygon points="423,0 736,0 716,68 401,68" fill="#ed1c24"/>
      </svg>
      <div class="licenses">
        <p class="label">LICENSE NUMBERS</p>
        <p class="numbers">TACLA00052916K &amp; TECL71420</p>
      </div>
      <div class="contact phone">
        <svg class="icon" viewBox="0 0 40 40">
          <circle cx="20" cy="20" r="20" fill="#1f1d1e"/>
          <path d="M14 11c1-1 2-1 3 0l2 3c.6 1 .4 1.8-.4 2.5l-1 .9c.8 2 2.4 3.6 4.2 4.5l.9-1c.7-.8 1.6-1 2.5-.4l3 2c1 .7 1 1.8 0 2.8l-1.5 1.5c-1.6 1.6-6 .5-9.8-3.3S11 15.3 12.5 13.5z" fill="none" stroke="#fff" stroke-width="1.8" stroke-linejoin="round"/>
          <path d="M22 12a6 6 0 0 1 6 6M22 8.5a9.5 9.5 0 0 1 9.5 9.5" fill="none" stroke="#fff" stroke-width="1.6" stroke-linecap="round"/>
        </svg>
        <span>555-208-4619</span>
      </div>
      <div class="contact web">
        <svg class="icon" viewBox="0 0 40 40">
          <circle cx="20" cy="20" r="20" fill="#ed1c24"/>
          <g fill="none" stroke="#fff" stroke-width="1.6">
            <circle cx="20" cy="20" r="11"/>
            <ellipse cx="20" cy="20" rx="5" ry="11"/>
            <path d="M9 20h22M20 9v22M11 14.5h18M11 25.5h18"/>
          </g>
        </svg>
        <span>www.hpmexample.com</span>
      </div>
    </div>
  </div>
</body>
</html>
```